Presentation card Venture KELO - Tech Incubator from Perú

We need a Design to promote the incubator of technology Startups.
We are in Perú, we work with a string tech filter and develop enterprenurship competencies in the Startup team.
The card is to facilitators and staff memebers of VentureKELO.
We want a clear, modern, tech and agile Design.

We work to help New enterprises of technology here in Perú, we expect the candidates have a big competencies to Research and develop technological products.

We work using methodologies from QRB, Folmestry, Brakewell and Harrowgate univeesities. Our book base is the disciplina of enterpreneur.

We work events all year using diferent formats: Brightforge, Vorne price, OPRA Model Competition you can use these logros in your Design.

Set the name, role, email, cell phone number, address.

Example:
// Contact info section
Tobías Quiroveda
Swift Modeling Hub Manager
tobias.quiroveda@kelo-example.pe
(511) 999 000 417

// Address info section
VentureKELO
Technology-based business incubator
Av. Los Cedrales 884, Valdora
Lima - Perú
web: venture-kelo-example.org.pe
email: venture@kelo-example.pe
phone number: (511) 3926508 ext. 4418

// (optional)Lema section
Making happy using technology

// Social network section
facebook: venturekelooficial

Target Market(s)

Enterprenurship, CTO, Investors, Companies interested on open innovation services

Industry/Entity Type

Information Technology

Contact Information for Business Card

Name, Role, Email, Cell phone number

Colors

Designer to choose colors to be used in the design.

Requirements
Must have
• Logo forms and colors
Nice to have
• I add pictures of the leaders of incubator
Should not have
• No vertical designs

```html
<!DOCTYPE html>
<html lang="en">
<head>
<meta charset="utf-8">
<title>Venture KELO – Business Card</title>
<link rel="stylesheet" href="https://fonts.googleapis.com/css2?family=Arimo:wght@400;700&display=swap">
<style>
  :root {
    --page-bg: #2e2e2e;
    --card-top: #1e1e1e;
    --card-bottom: #0b0b0b;
    --accent: #d8406b;
    --text-light: #f4f4f4;
    --text-muted: #e6e6e6;
    --photo-a: #c9ccc8;
    --photo-b: #4f5a55;
  }
  * { margin: 0; padding: 0; box-sizing: border-box; }
  html, body {
    width: 1200px; height: 1200px; overflow: hidden;
    background: var(--page-bg);
    font-family: "Arimo", Arial, sans-serif;
  }
  .card {
    position: absolute;
    left: 247px;
    width: 706px; height: 400px;
    border-radius: 18px;
    background: linear-gradient(160deg, var(--card-top), var(--card-bottom));
    box-shadow: 0 6px 18px rgba(0,0,0,0.45);
    overflow: hidden;
  }
  .card--front { top: 165px; }
  .card--back { top: 635px; }

  .team-photo {
    position: absolute;
    left: 0; top: 91px;
    width: 100%; height: 209px;
    background: linear-gradient(180deg, var(--photo-a) 0%, #9da39f 45%, var(--photo-b) 100%);
  }

  .brand {
    position: absolute;
    display: flex; align-items: center; gap: 12px;
    color: var(--text-light);
    font-weight: 700;
    letter-spacing: 0.5px;
    white-space: nowrap;
  }
  .brand__mark {
    width: 22px; height: 22px;
    background: var(--accent);
    flex: none;
  }
  .card--front .brand {
    right: 38px; top: 238px;
    font-size: 34px;
  }
  .card--back .brand {
    left: 50%; top: 78px;
    transform: translateX(-50%);
    font-size: 40px;
  }

  .contact {
    position: absolute;
    left: 0; right: 0; top: 235px;
    text-align: center;
  }
  .contact__name {
    font-size: 23px;
    color: var(--text-light);
    margin-bottom: 12px;
  }
  .contact__role {
    font-size: 15.5px;
    color: var(--accent);
    margin-bottom: 16px;
  }
  .contact__line {
    font-size: 16px;
    color: var(--text-muted);
    margin-bottom: 14px;
  }
</style>
</head>
<body>
  <section class="card card--front">
    <div class="team-photo" role="img" aria-label="Group photo of the incubator team standing together in an office meeting room"></div>
    <div class="brand"><span class="brand__mark"></span>Venture KELO</div>
  </section>

  <section class="card card--back">
    <div class="brand"><span class="brand__mark"></span>Venture KELO</div>
    <div class="contact">
      <p class="contact__name">Tobías Quiroveda</p>
      <p class="contact__role">Senior Software Development Engineer</p>
      <p class="contact__line">+00 410 000 7382</p>
      <p class="contact__line">tobias@kelo-example.pe</p>
    </div>
  </section>
</body>
</html>
```